Letterhead

We have a new logo and would like to design electronic letterhead with our new logo. We have two office locations. One of our offices is moving in July.

```html
<!DOCTYPE html>
<html lang="en">
<head>
<meta charset="utf-8">
<title>Halden Reed Letterhead</title>
<link rel="stylesheet" href="https://fonts.googleapis.com/css2?family=Source+Sans+3:wght@400;600&family=Arimo:wght@700&display=swap">
<style>
  :root {
    --backdrop: #e4e5e7;
    --paper: #ffffff;
    --ink-dark: #2b2d3a;
    --ink-body: #6d6f73;
    --brand-blue: #2d6db5;
    --footer-band: #2b2d3a;
  }
  * { box-sizing: border-box; margin: 0; padding: 0; }
  html, body { width: 1200px; height: 945px; overflow: hidden; }
  body {
    background: var(--backdrop);
    font-family: "Source Sans 3", "Myriad Pro", sans-serif;
    position: relative;
  }
  .letterhead {
    position: absolute;
    left: 282px; top: 22px;
    width: 636px; height: 900px;
    background: var(--paper);
    box-shadow: 0 4px 18px rgba(0,0,0,.12);
    overflow: hidden;
  }
  .contact-list {
    position: absolute; top: 44px; right: 62px;
    list-style: none;
    font-size: 10px; line-height: 12px;
    color: var(--ink-dark);
  }
  .contact-list li { display: flex; align-items: center; gap: 5px; }
  .contact-list svg { width: 8px; height: 8px; fill: var(--brand-blue); }
  .firm-name {
    position: absolute; top: 96px; left: 56px;
    font-size: 22px; font-weight: 600;
    color: var(--ink-dark);
    letter-spacing: .5px;
    display: flex; align-items: center; gap: 8px;
  }
  .firm-name .dot {
    width: 12px; height: 12px; background: var(--brand-blue);
  }
  .letter-body {
    position: absolute; top: 282px; left: 90px; width: 470px;
    color: var(--ink-body);
    font-size: 13.5px; line-height: 15.5px;
  }
  .salutation {
    font-family: "Arimo", Arial, sans-serif;
    font-weight: 700; font-size: 14px;
    color: #1e1f24;
    margin-bottom: 18px;
    margin-left: -24px;
  }
  .letter-body p { margin-bottom: 18px; }
  .letter-body p.indent { text-indent: 24px; }
  .signature {
    width: 150px; height: 48px; margin-top: 10px;
    background: linear-gradient(90deg, #eeeeee, #f6f6f6);
    border-radius: 4px;
  }
  .footer-band {
    position: absolute; left: 0; right: 0; bottom: 0; height: 6px;
    background: var(--footer-band);
  }
  .web-tab {
    position: absolute; bottom: 6px; right: 40px;
    height: 30px; width: 200px;
  }
  .web-tab svg { position: absolute; inset: 0; }
  .web-tab span {
    position: relative; display: block;
    text-align: center; line-height: 30px;
    color: #fff; font-size: 12px; letter-spacing: .6px;
  }
  .address {
    position: absolute; bottom: 14px; left: 48px;
    font-size: 11px; color: var(--ink-dark);
    display: flex; align-items: center; gap: 4px;
  }
  .address svg { width: 9px; height: 11px; fill: var(--brand-blue); }
</style>
</head>
<body>
  <article class="letterhead">
    <ul class="contact-list">
      <li><svg viewBox="0 0 10 10"><path d="M2 0l2 2-1 1.5c.8 1.5 2 2.7 3.5 3.5L8 6l2 2-1.5 2C4 9.5.5 6 0 1.5z"/></svg>+61 7 555 0148</li>
      <li><svg viewBox="0 0 10 10"><rect x="0" y="4" width="10" height="5" rx="1"/><rect x="2" y="1" width="6" height="3"/></svg>+61 7 555 0149</li>
      <li><svg viewBox="0 0 10 10"><path d="M0 2h10v6H0z M0 2l5 3 5-3" /></svg>info@haldenreed.com</li>
    </ul>

    <div class="firm-name"><span class="dot"></span>Halden Reed Attorneys at Law</div>

    <section class="letter-body">
      <p class="salutation">Dear Mr. John,</p>
      <p>Lorem Ipsum is simply dummy text of the printing and typesetting industry. Lorem Ipsum has been the industry's standard dummy text ever since the 1500s, when an unknown printer took a galley of type and scrambled it to make a type specimen book. It has survived not only five centuries, but also the leap into electronic typesetting, remaining essentially unchanged.</p>
      <p class="indent">The standard chunk of Lorem Ipsum used since the 1500s is reproduced below for those interested. Sections 1.10.32 and 1.10.33 from "de Ordine Verborum" by Marrow are also reproduced in their exact original form, accompanied by English versions from the 1914 translation by T. Wendell</p>
      <p class="indent">Lorem Ipsum is simply dummy text of the printing and typesetting industry. Lorem Ipsum has been the industry's standard dummy text ever since the 1500s, when an unknown printer took a galley of type and scrambled it to make a type specimen book. It has survived not only five centuries, but also the leap into electronic typesetting, remaining essentially unchanged. It was popularised in the</p>
      <div class="signature" role="img" aria-label="Handwritten signature of the sender"></div>
    </section>

    <div class="address">
      <svg viewBox="0 0 9 11"><path d="M4.5 0A4.5 4.5 0 0 0 0 4.5C0 8 4.5 11 4.5 11S9 8 9 4.5A4.5 4.5 0 0 0 4.5 0zm0 6.3a1.8 1.8 0 1 1 0-3.6 1.8 1.8 0 0 1 0 3.6z"/></svg>
      Po. box 201, Street Name, City Name, Zip Code - 00000
    </div>

    <div class="web-tab">
      <svg viewBox="0 0 200 30" preserveAspectRatio="none"><polygon points="8,0 180,0 200,30 0,30" fill="#2d6db5"/></svg>
      <span>www.haldenreed.com</span>
    </div>
    <div class="footer-band"></div>
  </article>
</body>
</html>
```